Beauty, Health & Skincare Medical Spa Needs wall sign design

We need signage made for our Edmonton based premium, multi-service high-end medical spa. The sign will be posted on a large brick wall on the side of our spa. The sign will be 10" High and 15" wide. It will be permanent. We offer cosmetic procedures like velarin, injectables, anti-aging treatments and fat reduction. Our spa colors are blue and purple. We offer a procedure called FrostShapeRx which is non-invasive fat reduction. We want the Frostshaperx logo featured on the sign. We want it to be sexy and eye catching. We want it to appeal to men and women. We were thinking of featuring a fit attractive woman or man or both on the ad.
Updates

Target Market(s)

women, men

Industry/Entity Type

Medical

Requirements
Must have
• Our logo, velarin, plumaxil and frostshaperx logo. Must have a picture of an woman and mans, less words are better as this will be high up and harder to read.
Should not have
• nothing day spa

```html
<!DOCTYPE html>
<html lang="en">
<head>
<meta charset="utf-8">
<title>Lumen Reverse – Medical Spa Wall Sign</title>
<link rel="stylesheet" href="https://fonts.googleapis.com/css2?family=Montserrat:wght@400;500;700&family=Titillium+Web:wght@600;700&display=swap">
<style>
  :root {
    --brand-blue: #3656a8;
    --brand-purple: #5b3a9c;
    --lavender-pale: #ece8f7;
    --lavender: #b3a8de;
    --lavender-deep: #8677c4;
    --rule-blue: #4aa3e0;
    --ink-white: #ffffff;
    --service-shadow: rgba(58, 38, 120, 0.9);
    --photo-light: #d9b9a3;
    --photo-mid: #a87a5f;
    --photo-dark: #4a3027;
    --partner-blue: #1c6fb8;
    --partner-mauve: #8c7a9a;
  }
  * { margin: 0; padding: 0; box-sizing: border-box; }
  html, body { width: 1200px; height: 849px; overflow: hidden; background: #ffffff; }
  .sign {
    position: relative;
    width: 1200px;
    height: 849px;
    overflow: hidden;
    background:
      linear-gradient(90deg, #ffffff 0%, rgba(255,255,255,0.85) 44%, rgba(255,255,255,0) 62%),
      linear-gradient(168deg, #ffffff 0%, #ffffff 24%, var(--lavender-pale) 38%, var(--lavender) 60%, var(--lavender-deep) 100%);
  }
  .portrait {
    position: absolute;
    left: 0; top: 0;
    width: 680px; height: 849px;
    background:
      radial-gradient(ellipse 45% 40% at 38% 42%, var(--photo-light) 0%, var(--photo-mid) 55%, var(--photo-dark) 100%);
    -webkit-mask-image: linear-gradient(90deg, #000 0%, #000 58%, transparent 92%);
    mask-image: linear-gradient(90deg, #000 0%, #000 58%, transparent 92%);
  }
  .focus-marks { position: absolute; left: 0; top: 0; }
  .header-rule {
    position: absolute; left: 540px; top: 190px;
    width: 660px; height: 2px;
    background: linear-gradient(90deg, rgba(74,163,224,0) 0%, var(--rule-blue) 30%, var(--rule-blue) 100%);
  }
  .brand {
    position: absolute; left: 612px; top: 66px;
    display: flex; align-items: center; gap: 18px;
  }
  .brand-mark {
    width: 58px; height: 58px;
    background: var(--brand-purple);
  }
  .brand-name {
    font-family: "Montserrat", sans-serif;
    font-weight: 500;
    font-size: 54px;
    color: var(--brand-blue);
    letter-spacing: -0.5px;
  }
  .headline {
    position: absolute; left: 580px; top: 226px;
    font-family: "Montserrat", sans-serif;
    font-weight: 400;
    font-size: 44px;
    line-height: 68px;
    color: var(--brand-blue);
  }
  .headline strong { font-weight: 700; color: var(--brand-purple); }
  .services {
    position: absolute; left: 570px; top: 404px;
    width: 580px;
    list-style: none;
    text-align: center;
    font-family: "Titillium Web", sans-serif;
    font-weight: 700;
    font-size: 46px;
    line-height: 62px;
    letter-spacing: 0.5px;
    color: var(--ink-white);
    text-shadow: 2px 3px 3px var(--service-shadow), 0 0 10px rgba(70,50,140,0.45);
  }
  .partner-strip {
    position: absolute; left: 330px; top: 724px;
    width: 870px; height: 88px;
    background: linear-gradient(90deg, rgba(255,255,255,0) 0%, #ffffff 10%, #ffffff 92%, rgba(255,255,255,0.6) 100%);
    border-bottom: 3px solid var(--brand-blue);
    display: flex; align-items: center;
    padding-left: 48px; gap: 34px;
  }
  .partner-badge {
    width: 70px; height: 70px; border-radius: 50%;
    background: var(--partner-blue);
    border: 4px solid #ffffff;
    box-shadow: 0 0 0 2px var(--partner-blue);
    flex: none;
  }
  .partner {
    display: flex; align-items: center; gap: 8px;
    font-family: "Montserrat", sans-serif;
    font-weight: 500;
    font-size: 28px;
  }
  .partner-dot { width: 26px; height: 26px; border-radius: 50%; flex: none; }
  .partner--frost { color: var(--partner-blue); }
  .partner--frost .partner-dot { background: var(--partner-blue); }
  .partner--plumaxil { color: var(--partner-mauve); }
  .partner--velarin { color: var(--brand-purple); font-size: 26px; }
</style>
</head>
<body>
  <main class="sign">
    <div class="portrait" role="img" aria-label="Close-up portrait photograph of a woman with brown hair, eyes and lips in sharp focus"></div>

    <svg class="focus-marks" width="620" height="849" viewBox="0 0 620 849" aria-hidden="true">
      <line x1="0" y1="191" x2="560" y2="191" stroke="#ffffff" stroke-width="2"/>
      <line x1="0" y1="510" x2="560" y2="510" stroke="#ffffff" stroke-width="2"/>
      <polygon points="330,172 346,172 338,184" fill="#ffffff"/>
      <polygon points="330,528 346,528 338,516" fill="#ffffff"/>
    </svg>

    <div class="brand">
      <span class="brand-mark" aria-hidden="true"></span>
      <span class="brand-name">Lumen Reverse</span>
    </div>
    <div class="header-rule"></div>

    <h1 class="headline">Premium, multi-service<br>high-end <strong>medical spa</strong></h1>

    <ul class="services">
      <li>VELARIN</li>
      <li>INJECTABLES</li>
      <li>ANTI-AGING TREATMENTS</li>
      <li>FAT REDUCTION</li>
    </ul>

    <div class="partner-strip">
      <span class="partner-badge" aria-hidden="true"></span>
      <span class="partner partner--frost"><span class="partner-dot" aria-hidden="true"></span>frostshaperx</span>
      <span class="partner partner--plumaxil">plumaxil</span>
      <span class="partner partner--velarin">velarin Cosmetic</span>
    </div>
  </main>
</body>
</html>
```